Box for a Bold Bathroom - stylish minimalist package for a modern upscale brand

We need an adaptable package design using a color label on a brown box, or just a brown box with 2 or 3 color printing. The best design would be one that is adaptable for either use.

Our first products launching under this brand will be a series of medicine cabinets and mirrors, and our cartons can vary in size from 500x100x600 mm to 1200x300x1000 mm

About us: we produce a variety of bathroom fixtures including medicine cabinets, mirrors, vanities, etc. You've likely seen our products - we do manufacturing for Valdrane, Murtello, Fenwick Hollow, Dunmore & Pike, and others.

A version of our logo is attached for reference; we use it in a variety of color mixes depending on application. Vector available if needed or can be used FPO and our team will replace.

These are our colors, please take note and ignore the 'color' field:

Light Blue: C:66%/M:6%/Y:22%/K:0%; H:189° S:65% B:78%
Light Grey: C:35%/M:26%/Y:24%/K:0%; H:213° S:5% B:70%
Dark Blue: C:90%/M:50%/Y:44%/K:20%; H:189° S:82% B:43%
Dark Grey: C:70%/M:60%/Y:54%/K:38%; H:213° S:11% B:30%

Project Deadline Extended
Reason: Some revisions still outstanding before we can make selection, and some submissions we have agreed to wait for. Please submit all work ASAP so our team can provide feedback to you. Thanks!

Target Market(s)

DIY'ers; home renovators

Industry/Entity Type

Home Improvement

Font styles to use
Sans Serif

Requirements
Must have
• 1. Brand logo w/ logotype
• 2. Brand name without logo (can be on shipping mark side)
• 3. Multi-lingual En/Fr/Es (you do not need to include multi-lingual content but must allow space for our own translations if you do not)
• 4. Shipping/Handling Glyphs on 5 sides (all but bottom)
• i.e. fragile, this way up, team lift or mech lift, clamp or no clamp, max-stack
• 5. Two sides should include a marked 4" x 4" area for affixing labels (e.g. UPC, SSCC, etc.) ideally with a dotted line or corner marks or similar.
• 6. Shipping mark details or space for them (should be on the smallest side, only needed on one but can be on both) [see example file of shipping mark informations]
Nice to have
• Design that can be used either with color label on brown box, or brown box only.
• If designing for color label; please see the sample images included. Lifestyle should be prominent, the inside photo being smaller to help show interior features. These photos are obviously not useful for brown-box design.

```html
<!DOCTYPE html>
<html lang="en">
<head>
<meta charset="utf-8">
<title>Slatemere – Carton Dieline</title>
<link rel="stylesheet" href="https://fonts.googleapis.com/css2?family=Montserrat:ital,wght@0,400;0,600;0,700;1,700&display=swap">
<style>
  :root {
    --bg-edge: #195d6c;
    --bg-center: #3a7482;
    --dark-blue: #1c6272;
    --light-blue: #3fb8c8;
    --dark-grey: #45484d;
    --light-grey: #e5e6e8;
    --info-fill: #cadbe3;
    --glyph-fill: #d3d5d8;
    --panel: #ffffff;
    --crease: #9aa3a8;
  }
  html, body { margin: 0; padding: 0; width: 1200px; height: 1200px; overflow: hidden; }
  body {
    background: radial-gradient(circle at 50% 50%, var(--bg-center) 0%, var(--bg-edge) 75%);
    font-family: "Montserrat", sans-serif;
  }
  .dieline { display: block; width: 1200px; height: 1200px; }
  .panel { fill: var(--panel); stroke: var(--crease); stroke-width: 0.8; }
  .dust-flap { fill: var(--light-grey); stroke: var(--crease); stroke-width: 0.8; }
  .crease { stroke: var(--crease); stroke-width: 0.8; fill: none; }
  .brand-band { fill: var(--dark-blue); }
  .brand-name { fill: var(--dark-grey); font-family: "Montserrat", sans-serif; font-weight: 600; letter-spacing: 1.5px; }
  .brand-name-light { fill: var(--dark-grey); font-family: "Montserrat", sans-serif; font-weight: 400; letter-spacing: 2px; }
  .tagline { fill: var(--dark-grey); font-family: "Montserrat", sans-serif; font-weight: 700; font-style: italic; font-size: 19px; letter-spacing: 0.5px; }
  .info-panel { fill: var(--info-fill); }
  .info-frame { fill: none; stroke: var(--dark-grey); stroke-width: 0.8; }
  .info-text { fill: var(--dark-grey); font-family: "Montserrat", sans-serif; font-size: 6.4px; font-weight: 600; }
  .label-zone { fill: #fff; stroke: var(--dark-grey); stroke-width: 1.4; stroke-dasharray: 3 2; }
  .label-corner { fill: none; stroke: var(--dark-grey); stroke-width: 2.5; }
  .glyph-tile { fill: var(--glyph-fill); }
  .glyph-ink { fill: none; stroke: var(--dark-grey); stroke-width: 2.4; stroke-linecap: square; }
  .glyph-solid { fill: var(--dark-grey); }
  .glyph-num { fill: var(--dark-grey); font-family: "Montserrat", sans-serif; font-weight: 700; font-size: 15px; }
</style>
</head>
<body>
<svg class="dieline" viewBox="0 0 1500 1500" xmlns="http://www.w3.org/2000/svg">
  <defs>
    <linearGradient id="lifestyle-tone" x1="0" y1="0" x2="0" y2="1">
      <stop offset="0" stop-color="#aebfc8"/>
      <stop offset="0.33" stop-color="#dfe7eb"/>
      <stop offset="0.55" stop-color="#f1f5f7"/>
      <stop offset="0.72" stop-color="#8fa7b3"/>
      <stop offset="1" stop-color="#6f8b99"/>
    </linearGradient>
    <clipPath id="front-clip"><rect x="303" y="325" width="894" height="425"/></clipPath>
    <clipPath id="back-clip">
      <path d="M505 953 L995 953 L1140 985 Q1172 995 1172 1030 L1172 1320 Q1172 1345 1140 1355 L995 1380 L505 1380 L360 1355 Q328 1345 328 1320 L328 1030 Q328 995 360 985 Z"/>
    </clipPath>

    <g id="handling-glyphs">
      <rect class="glyph-tile" x="0" y="0" width="32" height="30"/>
      <path class="glyph-ink" d="M10 22 V9 M6 13 L10 8 L14 13 M22 22 V9 M18 13 L22 8 L26 13 M6 25 H26"/>
      <rect class="glyph-tile" x="36" y="0" width="32" height="30"/>
      <path class="glyph-ink" d="M44 12 L52 8 L60 12 L52 16 Z M44 12 V21 L52 25 L60 21 V12 M52 16 V25"/>
      <rect class="glyph-tile" x="72" y="0" width="32" height="30"/>
      <path class="glyph-solid" d="M80 5 H96 Q96 18 89 19 V24 H93 V26 H83 V24 H87 V19 Q80 18 80 5 Z"/>
      <rect class="glyph-tile" x="108" y="0" width="32" height="30"/>
      <path class="glyph-ink" d="M116 8 H132 V22 H116 Z M116 8 L132 22 M132 8 L116 22"/>
      <path class="glyph-solid" d="M109 15 L113 12 V18 Z M139 15 L135 12 V18 Z"/>
      <rect class="glyph-tile" x="144" y="0" width="32" height="30"/>
      <text class="glyph-num" x="160" y="21" text-anchor="middle">10</text>
      <path class="glyph-ink" d="M150 25 H170"/>
    </g>

    <g id="front-art">
      <rect role="img" aria-label="Lifestyle photograph of a modern vanity with a dark vessel sink and chrome faucet" x="530" y="325" width="465" height="350" fill="url(#lifestyle-tone)"/>
      <path d="M383 325 Q560 625 1197 676 L1197 760 L303 760 L303 325 Z" fill="#fff"/>
      <path class="brand-band" d="M383 325 Q560 625 1197 672 L1197 693 Q540 660 383 325 Z"/>
      <text class="brand-name" x="543" y="412" font-size="11">SLATEMERE</text>
      <use href="#handling-glyphs" x="530" y="701"/>
      <rect class="label-zone" x="929" y="687" width="46" height="46"/>
      <path class="label-corner" d="M927 695 V685 H937 M967 685 H977 V695 M977 725 V735 H967 M937 735 H927 V725"/>
    </g>
  </defs>

  <!-- top tuck flap and lid -->
  <path class="panel" d="M508 122 V105 Q508 85 530 85 H970 Q992 85 992 105 V122 Z"/>
  <path class="dust-flap" d="M312 127 L505 122 V323 L312 320 Z"/>
  <path class="dust-flap" d="M995 122 L1188 127 V320 L995 323 Z"/>
  <rect class="panel" x="505" y="122" width="490" height="201"/>
  <g class="lid-text" transform="rotate(180 750 210)">
    <text class="tagline" x="750" y="226" text-anchor="middle">STYLISH BATHROOM FIXTURES</text>
    <text class="brand-name" x="750" y="202" text-anchor="middle" font-size="9">SLATEMERE</text>
  </g>

  <!-- main row -->
  <path class="panel" d="M122 325 H303 V750 H122 V645 L118 645 Q112 645 112 638 V438 Q112 430 118 430 H122 Z"/>
  <path class="panel" d="M1197 325 H1378 V430 H1382 Q1388 430 1388 438 V638 Q1388 645 1382 645 H1378 V750 H1197 Z"/>
  <rect class="panel" x="303" y="325" width="894" height="425"/>
  <g clip-path="url(#front-clip)"><use href="#front-art"/></g>
  <path class="crease" d="M505 325 V750 M995 325 V750"/>

  <!-- left end panel: shipping mark -->
  <rect class="info-panel" x="342" y="444" width="125" height="248" rx="2"/>
  <rect class="info-frame" x="346" y="452" width="116" height="83"/>
  <g class="info-text">
    <text x="351" y="462">LOT #</text><text x="382" y="462">: 12340506</text>
    <text x="351" y="470">ITEM #</text><text x="382" y="470">: XXX00000A</text>
    <text x="351" y="479">DIM</text><text x="382" y="479">: 109.2 X 45.1 X 95.9 CM</text>
    <text x="386" y="488">(43" X 17" X 37")</text>
    <text x="351" y="497">NW / PN</text><text x="382" y="497">:         KG (       LB)</text>
    <text x="351" y="506">GW / PB</text><text x="382" y="506">:         KG (       LB)</text>
    <text x="351" y="514">CUBE</text><text x="382" y="514">: 99.449 M  (999.9FT)</text>
    <text x="351" y="523">QTY</text><text x="382" y="523">: 1</text>
    <text x="351" y="531">CASE</text><text x="382" y="531">:</text>
  </g>
  <g transform="rotate(-90 321 630)">
    <text class="brand-name" x="321" y="634" text-anchor="middle" font-size="9">SLATEMERE</text>
  </g>
  <use href="#handling-glyphs" transform="translate(340 708) scale(0.72)"/>

  <!-- right end panel -->
  <g transform="rotate(90 1172 400)">
    <text class="brand-name" x="1172" y="404" text-anchor="middle" font-size="9">SLATEMERE</text>
  </g>
  <use href="#handling-glyphs" transform="translate(1031 708) scale(0.72)"/>

  <!-- bottom panel -->
  <path class="dust-flap" d="M312 755 L505 752 V952 L312 950 Z"/>
  <path class="dust-flap" d="M995 752 L1188 755 V950 L995 952 Z"/>
  <rect class="panel" x="505" y="752" width="490" height="201"/>
  <text class="brand-name-light" transform="rotate(180 750 853)" x="750" y="860" text-anchor="middle" font-size="18">SLATEMERE</text>

  <!-- back panel -->
  <path class="panel" d="M505 953 L995 953 L1140 985 Q1172 995 1172 1030 L1172 1320 Q1172 1345 1140 1355 L995 1380 L818 1380 L818 1403 Q818 1415 805 1415 L698 1415 Q685 1415 685 1403 L685 1380 L505 1380 L360 1355 Q328 1345 328 1320 L328 1030 Q328 995 360 985 Z"/>
  <g clip-path="url(#back-clip)">
    <use href="#front-art" transform="rotate(180 750 851.5)"/>
  </g>
  <path class="crease" d="M505 953 V1380 M995 953 V1380 M685 1380 H818"/>
</svg>
</body>
</html>
```